CPA Firm Business Card
Halvorin, Bestwick & Pardue CPAs, LLC
Project: CPA Firm Business Card
CPA Firm Business Card - Financial Services
Creative Brief
Professional
Moss Brandley, CPA
2867 E. Sable Way, Suite 348 Tucson, AZ 85619
moss@quillledger.net
In addition to business cards design I would also like to see designs for letterheads, envelopes and fax cover sheets.

```html
<!DOCTYPE html>
<html lang="en">
<head>
<meta charset="utf-8">
<title>Halvorin, Bestwick &amp; Pardue CPAs, LLC — Business Card</title>
<link rel="stylesheet" href="https://fonts.googleapis.com/css2?family=Roboto:wght@400;700&family=Roboto+Condensed:wght@700&display=swap">
<style>
  :root {
    --stage: #d9d9db;
    --card: #ffffff;
    --wine: #7d1a1f;
    --wine-deep: #5e1216;
    --slate-light: #b9babc;
    --ink: #4a4a4c;
  }
  * { box-sizing: border-box; margin: 0; padding: 0; }
  html, body { width: 1200px; height: 864px; overflow: hidden; }
  body {
    background: var(--stage);
    font-family: "Roboto", Arial, sans-serif;
    position: relative;
  }
  .card {
    position: absolute;
    width: 540px;
    height: 310px;
    background: var(--card);
    border-radius: 22px;
    box-shadow: 0 6px 18px rgba(0,0,0,0.18);
    overflow: hidden;
  }
  .card--front { left: 40px; top: 277px; }
  .card--back { left: 620px; top: 277px; }

  /* Front */
  .brand {
    position: absolute;
    left: 0; right: 0; top: 92px;
    display: flex;
    flex-direction: column;
    align-items: center;
  }
  .brand-mark {
    width: 30px; height: 30px;
    background: var(--wine);
    margin-bottom: 16px;
  }
  .brand-name {
    font-family: "Roboto Condensed", "Arial Narrow", sans-serif;
    font-weight: 700;
    font-size: 26px;
    line-height: 1.1;
    text-align: center;
    text-transform: uppercase;
    color: var(--wine);
  }
  .front-web {
    position: absolute;
    left: 0; right: 0; top: 226px;
    text-align: center;
    font-size: 12px;
    letter-spacing: 3px;
    color: var(--wine);
  }

  /* Back */
  .firm-name {
    position: absolute;
    left: 34px; top: 38px;
    width: 230px;
    font-family: "Roboto Condensed", "Arial Narrow", sans-serif;
    font-weight: 700;
    font-size: 21px;
    line-height: 1.05;
    text-transform: uppercase;
    color: var(--wine);
  }
  .firm-rule {
    position: absolute;
    left: 34px; top: 144px;
    width: 230px; height: 2px;
    background: var(--slate-light);
  }
  .contact-list {
    position: absolute;
    left: 292px; top: 40px;
    list-style: none;
    font-size: 12px;
    color: var(--ink);
  }
  .contact-list li {
    display: flex; align-items: center;
    height: 20px;
  }
  .contact-icon {
    width: 14px; height: 14px;
    border-radius: 50%;
    background: var(--wine);
    margin-right: 8px;
    display: inline-flex; align-items: center; justify-content: center;
  }
  .contact-icon svg { width: 8px; height: 8px; fill: #fff; }
  .person-name {
    position: absolute;
    left: 34px; top: 172px;
    font-weight: 700;
    font-size: 14px;
    color: var(--wine);
  }
  .address {
    position: absolute;
    left: 34px; top: 198px;
    font-size: 11px;
    line-height: 1.45;
    color: var(--ink);
  }
  .swoosh {
    position: absolute;
    left: 0; top: 0;
    width: 540px; height: 310px;
  }
</style>
</head>
<body>

  <section class="card card--front">
    <div class="brand">
      <span class="brand-mark" aria-hidden="true"></span>
      <div class="brand-name">Halvorin, Bestwick<br>&amp; Pardue</div>
    </div>
    <div class="front-web">www.hbpcpas.net</div>
  </section>

  <section class="card card--back">
    <svg class="swoosh" viewBox="0 0 540 310" aria-hidden="true">
      <path d="M540 150 C470 200 390 250 250 310 L540 310 Z" fill="var(--slate-light)"/>
      <path d="M540 190 C480 240 410 280 340 310 L540 310 Z" fill="var(--wine)"/>
      <path d="M540 240 C500 270 470 290 430 310 L540 310 Z" fill="var(--wine-deep)"/>
    </svg>

    <div class="firm-name">Halvorin, Bestwick &amp; Pardue CPAs, LLC</div>
    <div class="firm-rule"></div>

    <ul class="contact-list">
      <li><span class="contact-icon"><svg viewBox="0 0 10 10"><path d="M2 1h2l1 2-1 1c.5 1 1 1.5 2 2l1-1 2 1v2c-4 1-8-3-7-7z"/></svg></span>520-555-0142</li>
      <li><span class="contact-icon"><svg viewBox="0 0 10 10"><rect x="2" y="1" width="6" height="3"/><rect x="1" y="4" width="8" height="4"/></svg></span>520-555-0187</li>
      <li><span class="contact-icon"><svg viewBox="0 0 10 10"><path d="M1 2h8v6H1z M1 2l4 3 4-3" fill="none" stroke="#fff" stroke-width="1.2"/></svg></span>moss@quillledger.net</li>
      <li><span class="contact-icon"><svg viewBox="0 0 10 10"><circle cx="5" cy="5" r="3.6" fill="none" stroke="#fff" stroke-width="1.2"/></svg></span>www.hbpcpas.net</li>
    </ul>

    <div class="person-name">Moss Brandley, CPA</div>
    <div class="address">2867 E. Sable Way, Suite 348<br>Tucson, AZ 85619</div>
  </section>

</body>
</html>
```